Writer needs a book cover depicting 50-year old sassy & sexy psychotherapist on a quest to find love

I'm a writer who's preparing to self publish my first novel, *Plan
Zed. *When the realization that she’s lived over half a century lights a
fire under Helen Kowalczyk’s rapidly aging but still shapely* tush, *she
decides it’s time to take a new approach to dating –one drawn from her
training as a psychotherapist. Determined to avoid the romantic
mistakes she’s made in the past, she launches an intriguing research
project on Chatterly. When “Plan Zed” (as in “ex-boyfriends”)
unexpectedly turns Helen into Philadelphia’s radio relationship-guru
sensation, she attracts the attention of Curtis Ledbetter, a jaded
food-critic-turned-investigative reporter who assumes a fake identity as
a new therapy client in an effort to unmask her as a fraud.

The category is women's commercial fiction; the genre is "hen lit" (or
boomer lit)-- i.e., women's fiction targeted for women in their 40s-60s.

I envision a whimsical cover in vivid colors -- fuchsia perhaps, with
accents of yellow, blue and/or green. Helen Kowalczyk should be depicted as a
mature, somewhat frazzled woman who is very attractive & shapely. One possibility for the design could be that she's seated at her computer -- which is positioned over the title, PLAN ZED --daydreaming about the responses she's received to her ad. I envision
thought bubbles over her head. One bubble reads: Derek T. -- Loser!
Another says: Owen P. -- Brantonesque. Another bubble: Glenn R. -- sweet
but bald. Silhouettes of middle-aged men waiting in line to talk to Helen
bleed onto the back cover.

Since Helen becomes a radio talk show host and leaps to local celebrity in the Philadelphia area where she lives, a second possibility for the cover design is that she is seated at a radio console, sending advice over the airwaves to the single people (mostly men) who call into her show. I'd love to see the silhouettes of men somewhere on the cover -- perhaps at the top or bottom? -- representing the many callers who seek her guidance.

Although there are some serious moments in Plan Zed, it's mostly light-hearted and fun, and I'd like to convey that through use of whimsy, color scheme and type face.

Preferred color palette is whimsical, happy, and vivid. Please see attached photos as inspiration.

Target Market(s)

This is a genre called "hen lit" The target market is women in their late 30s to 60s. It's an offshoot of "chick lit" - aimed toward more mature maket.

Industry/Entity Type

Computer

Font styles to use
Serif

Requirements
Must have
• The main character must look mature -- not in her 20s or 30s. She's attractive, though, & has some pizazz. She's a white woman with dark, curly hair who's just turned 50.
Nice to have
• Modern, upbeat design with lots of flair. Bright colors --- feeling of optimism & definitely HUMOR!
Should not have
• The design should not look old-fashioned or "prissy."

```html
<!DOCTYPE html>
<html lang="en">
<head>
<meta charset="UTF-8">
<title>Plan Zed — Book Cover</title>
<link rel="stylesheet" href="https://fonts.googleapis.com/css2?family=Fredoka:wght@600&family=Varela+Round&family=Great+Vibes&display=swap">
<style>
  :root {
    --sky: #3fb2ee;
    --wine: #8c2233;
    --snow: #ffffff;
    --desk: #fdf5f8;
    --string-dark: #7a1e2c;
    --string-light: #ffffff;
    --name-blue: #3aa6e0;
    --skin: #f4c49b;
    --hair: #a8262d;
    --top: #c9b2dc;
    --laptop: #e8ecf8;
  }
  * { box-sizing: border-box; margin: 0; padding: 0; }
  html, body { width: 800px; height: 1200px; overflow: hidden; background: var(--sky); }

  .cover {
    position: relative;
    width: 800px;
    height: 1200px;
    background: var(--sky);
    overflow: hidden;
  }

  /* Hanging title */
  .title {
    position: absolute;
    top: 0;
    left: 52px;
    display: flex;
    align-items: flex-start;
    font-family: "Fredoka", "Varela Round", sans-serif;
    font-weight: 600;
    font-size: 172px;
    line-height: 1;
  }
  .title .word { display: flex; }
  .title .word + .word { margin-left: 44px; }
  .tile {
    position: relative;
    display: block;
    padding-top: 96px;
  }
  .tile::before {
    content: "";
    position: absolute;
    top: 0;
    left: 50%;
    width: 3px;
    height: 128px;
    transform: translateX(-50%);
    background: currentColor;
  }
  .tile::after {
    content: "";
    position: absolute;
    top: 122px;
    left: 50%;
    width: 10px;
    height: 10px;
    transform: translateX(-50%);
    border: 3px solid currentColor;
    border-radius: 50%;
    background: var(--sky);
  }
  .word-plan { color: var(--wine); }
  .word-zed { color: var(--snow); }
  .tile.drop-1 { padding-top: 110px; }
  .tile.drop-2 { padding-top: 88px; }

  /* Thought bubbles */
  .thoughts {
    position: absolute;
    inset: 0;
    width: 800px;
    height: 1200px;
  }
  .bubble-fill { fill: var(--snow); }
  .thought-name {
    font-family: "Varela Round", sans-serif;
    font-size: 22px;
    fill: var(--name-blue);
    text-anchor: middle;
  }
  .thought-note {
    font-family: "Varela Round", sans-serif;
    font-size: 22px;
    fill: var(--wine);
    text-anchor: middle;
  }

  /* Desk band */
  .desk {
    position: absolute;
    left: 87px;
    right: 0;
    top: 963px;
    bottom: 27px;
    background: var(--desk);
  }

  /* Heroine at laptop */
  .heroine {
    position: absolute;
    left: 225px;
    top: 540px;
    width: 350px;
    height: 500px;
    border-radius: 160px 160px 24px 24px;
    background: linear-gradient(180deg, var(--hair) 0%, var(--skin) 34%, var(--top) 62%, var(--laptop) 100%);
  }

  .author {
    position: absolute;
    left: 87px;
    right: 0;
    top: 1080px;
    text-align: center;
    font-family: "Great Vibes", cursive;
    font-size: 88px;
    line-height: 1;
    color: var(--wine);
  }
</style>
</head>
<body>
  <main class="cover">
    <h1 class="title" aria-label="Plan Zed">
      <span class="word word-plan">
        <span class="tile drop-1">P</span>
        <span class="tile">l</span>
        <span class="tile drop-2">a</span>
        <span class="tile drop-1">n</span>
      </span>
      <span class="word word-zed">
        <span class="tile drop-2">Z</span>
        <span class="tile drop-1">e</span>
        <span class="tile">d</span>
      </span>
    </h1>

    <svg class="thoughts" viewBox="0 0 800 1200" aria-hidden="false">
      <!-- left bubble -->
      <g class="bubble bubble-left">
        <g class="bubble-fill">
          <circle cx="135" cy="420" r="44"/>
          <circle cx="185" cy="385" r="50"/>
          <circle cx="240" cy="395" r="44"/>
          <circle cx="270" cy="435" r="38"/>
          <circle cx="240" cy="472" r="40"/>
          <circle cx="180" cy="478" r="44"/>
          <circle cx="118" cy="460" r="34"/>
          <ellipse cx="192" cy="430" rx="100" ry="52"/>
          <circle cx="222" cy="548" r="18"/>
          <circle cx="240" cy="590" r="12"/>
          <circle cx="262" cy="620" r="8"/>
        </g>
        <text class="thought-name" x="192" y="418">Owen P.</text>
        <text class="thought-note" x="192" y="450">-- Brantonesque</text>
      </g>
      <!-- middle bubble -->
      <g class="bubble bubble-middle">
        <g class="bubble-fill">
          <circle cx="365" cy="365" r="30"/>
          <circle cx="405" cy="345" r="36"/>
          <circle cx="440" cy="370" r="30"/>
          <circle cx="425" cy="405" r="30"/>
          <circle cx="380" cy="405" r="30"/>
          <ellipse cx="402" cy="380" rx="58" ry="36"/>
          <circle cx="402" cy="460" r="14"/>
          <circle cx="410" cy="500" r="9"/>
        </g>
        <text class="thought-name" x="402" y="374" style="font-size:19px">Derek T.</text>
        <text class="thought-note" x="402" y="400" style="font-size:19px">-- Loser!</text>
      </g>
      <!-- right bubble -->
      <g class="bubble bubble-right">
        <g class="bubble-fill">
          <circle cx="585" cy="450" r="36"/>
          <circle cx="630" cy="420" r="44"/>
          <circle cx="680" cy="440" r="38"/>
          <circle cx="700" cy="485" r="34"/>
          <circle cx="665" cy="522" r="36"/>
          <circle cx="612" cy="522" r="38"/>
          <circle cx="572" cy="490" r="30"/>
          <ellipse cx="636" cy="470" rx="76" ry="52"/>
          <circle cx="560" cy="588" r="15"/>
          <circle cx="538" cy="625" r="10"/>
        </g>
        <text class="thought-name" x="636" y="442">Glenn R.</text>
        <text class="thought-note" x="636" y="474">-- sweet</text>
        <text class="thought-note" x="636" y="504">but bald</text>
      </g>
    </svg>

    <div class="desk"></div>

    <div class="heroine" role="img" aria-label="Illustration of a red-haired woman in a lilac top sitting at a white laptop, gazing up at her thought bubbles"></div>

    <p class="author">Maren J. Holloway</p>
  </main>
</body>
</html>
```